KT Prime Motion personal training needs a new Business Card design for 2016

Business Card design:
Our current business card is very plain
We are bringing on our first team member next year and thought its a perfect time to have a new face lift for our company!

We are a Personal Training business "KT Prime Motion" who specializes in strength and conditioning / weightloss training,
We also run a yearly Bootcamp called "Ferocity Drillcamps", this is our Logo Design which we are looking for

The pink and blue in the logo are our business colours, how ever we don't want those colours to heavily dominate the card.

We are looking for a business card which is eye catching, and creative.

I am open to suggestions and any designs :)

Logo Design:

For our Logo Design we are looking for a bright, energetic logo, preferably a word logo which portrays strength and high intensity
If it has icon's etc in it thats fine again im open for suggestions :)
The Logo Design is for our Bootcamp which runs yearly
The bootcamp is called "Ferocity Drillcamp"

Target Market(s)

Age 20-40
Individuals who want to look great and have more energy

Industry/Entity Type

Business

Contact Information for Business Card

On the front
KT Prime Motion Doriel Maxton Personal Training / Bootcamps / Pilates / Nutrition Healthy mind, Healthy body, Ultimate lifestyle < our slogan
Icons for the following
Email:
Mobile:
Facebook:
Instagram:

On the back we would like to include somewhere
"Show this card to receive 50% off your first 30min pt session"
"Valid to one user only"

Logo Text

Ferocity Drillcamp

Font styles to use
Serif

Colors
e34197
0255a3
000000
ffffff

Requirements
Must have
• - Icons for instagram, facebook, email and mobile phone
• - Slogan: Healthy mind, Healthy body, Ultimate lifestyle
• - What we offer: Personal Training , Bootcamps, Pilates, Nutrition
• - Logo
• -
Nice to have
• - Our 50% offer on the back
• - a place for a photo
Should not have
• - Pink and Blue everywhere

```html
<!DOCTYPE html>
<html lang="en">
<head>
<meta charset="utf-8">
<title>KT Prime Motion – Business Card</title>
<link rel="stylesheet" href="https://fonts.googleapis.com/css2?family=Saira+Semi+Condensed:wght@400;500;700&display=swap">
<style>
  :root {
    --bg: #d9d6d3;
    --card: #121213;
    --card-edge: #1c1c1e;
    --pink: #e34197;
    --blue: #0255a3;
    --blue-bright: #2f7bd0;
    --white: #ffffff;
    --grey: #a9a9ad;
    --gloss: #3a3a3e;
    --rule: #55555a;
    --contact: #e6e6e8;
  }
  * { margin: 0; padding: 0; box-sizing: border-box; }
  html, body { width: 1200px; height: 814px; overflow: hidden; }
  body {
    background: var(--bg);
    font-family: "Saira Semi Condensed", "Arial Narrow", sans-serif;
    position: relative;
  }
  .card {
    position: absolute;
    top: 257px;
    width: 525px;
    height: 300px;
    background: var(--card);
    border: 1px solid var(--card-edge);
    box-shadow: 0 10px 26px rgba(0,0,0,.28);
    color: var(--white);
    overflow: hidden;
  }
  .card p, .card li { white-space: nowrap; line-height: 1.2; }
  .card--back { left: 50px; }
  .card--front { left: 625px; }

  .brand-mark {
    position: absolute;
    display: flex;
    align-items: center;
    gap: 12px;
    white-space: nowrap;
  }
  .brand-dot { border-radius: 50%; flex: none; }
  .brand-name { font-weight: 700; text-transform: uppercase; letter-spacing: .5px; line-height: 1; }

  /* back */
  .card--back .brand-mark { left: 50%; top: 62px; transform: translateX(-50%); }
  .card--back .brand-dot { width: 46px; height: 46px; background: var(--gloss); }
  .card--back .brand-name { font-size: 32px; color: var(--gloss); }

  .slogan {
    position: absolute; left: 48px; right: 48px; top: 148px;
    font-size: 14px; font-weight: 500; letter-spacing: .3px;
    text-transform: uppercase; color: #d8d8da;
  }
  .slogan-rule {
    position: absolute; left: 48px; right: 48px; top: 172px;
    height: 1px; background: var(--rule);
  }
  .offer {
    position: absolute; left: 48px; right: 48px; top: 182px;
    font-size: 14px; color: var(--grey);
  }
  .offer strong { color: var(--white); font-size: 17px; font-weight: 700; }
  .offer-note {
    position: absolute; left: 48px; right: 48px; top: 208px;
    font-size: 12px; color: var(--grey); text-align: center;
  }

  /* front */
  .card--front .brand-mark { left: 130px; top: 70px; }
  .card--front .brand-dot { width: 52px; height: 52px; background: var(--blue); }
  .card--front .brand-name { font-size: 30px; color: var(--blue-bright); }

  .person { position: absolute; left: 30px; top: 156px; width: 205px; text-align: right; }
  .person-name { font-size: 18px; font-weight: 500; color: var(--blue-bright); text-transform: uppercase; }
  .person-role { font-size: 15px; color: var(--pink); text-transform: uppercase; margin-top: 3px; }

  .divider { position: absolute; left: 250px; top: 152px; width: 1px; height: 76px; background: var(--rule); }

  .contacts { position: absolute; left: 266px; top: 152px; list-style: none; }
  .contacts li { display: flex; align-items: center; gap: 10px; font-size: 14px; color: var(--contact); height: 25px; }
  .contacts svg { width: 15px; height: 15px; flex: none; }

  .services {
    position: absolute; left: 0; right: 0; top: 252px;
    font-size: 15px; font-weight: 700; text-transform: uppercase; letter-spacing: .2px;
    color: var(--white); text-align: center;
  }
</style>
</head>
<body>

<section class="card card--back" aria-label="Business card back">
  <div class="brand-mark">
    <span class="brand-dot"></span>
    <span class="brand-name">KT Prime Motion</span>
  </div>
  <p class="slogan">Healthy Mind | Healthy Body | Ultimate Lifestyle</p>
  <div class="slogan-rule"></div>
  <p class="offer">Show this card to receive <strong>50% off</strong> your first 30min pt session</p>
  <p class="offer-note">Valid to one user only</p>
</section>

<section class="card card--front" aria-label="Business card front">
  <div class="brand-mark">
    <span class="brand-dot"></span>
    <span class="brand-name">KT Prime Motion</span>
  </div>

  <div class="person">
    <p class="person-name">Doriel Maxton</p>
    <p class="person-role">CEO/Founder</p>
  </div>

  <div class="divider"></div>

  <ul class="contacts">
    <li>
      <svg viewBox="0 0 16 16" aria-hidden="true"><rect x="4" y="1" width="8" height="14" rx="1.5" fill="none" stroke="#2f7bd0" stroke-width="1.5"/><circle cx="8" cy="12.5" r="0.9" fill="#2f7bd0"/></svg>
      555 204 7190
    </li>
    <li>
      <svg viewBox="0 0 16 16" aria-hidden="true"><rect x="1" y="3" width="14" height="10" rx="1" fill="#2f7bd0"/><path d="M1.5 3.8 8 9l6.5-5.2" fill="none" stroke="#121213" stroke-width="1.3"/></svg>
      hello@ktprimemotion.example
    </li>
    <li>
      <svg viewBox="0 0 16 16" aria-hidden="true"><circle cx="8" cy="8" r="7" fill="#2f7bd0"/><path d="M1 8h14M8 1c-3 3.5-3 10.5 0 14M8 1c3 3.5 3 10.5 0 14" fill="none" stroke="#121213" stroke-width="1"/></svg>
      www.ktprimemotion.example
    </li>
  </ul>

  <p class="services">Personal Training | Bootcamps | Pilates | Nutrition</p>
</section>

</body>
</html>
```